Tallow & Mersey Needs New Stationery / Letterhead Design

We need new stationery to match our new logo (attached). Tallow & Mersey is a 34 year old nationwide law firm located in Houston Tx. They do personal injury law and pharmaceutical litigation.

WE DO NOT NEED BUSINESS CARDS.

Attached are several different file formats of the new logo.

Reason: We will make a decision in the next couple days. Finalizing edits now. Thank you!

Target Market(s)

consumers who have been injured due to the negligence of another or by a pharmaceutical drug or defective medical device. Also co-counsel and opposing counsel (law firms0.

Industry/Entity Type

Law Firm

Requirements
Must have
• logo
• Tallow & Mersey, LLP
• 7183 Corvid Lane, Suite 640
• Brenford, OK 75591
• Tel: (555) 408-1936
• Fax: (555) 408-2275
• www.tallowandmersey.example
• Must have colors in the logo.
• Make the font go with the logo - not necessarily the same, but something that goes well with it.

```html
<!DOCTYPE html>
<html lang="en">
<head>
<meta charset="utf-8">
<title>Tallow &amp; Mersey — Letterhead</title>
<link rel="stylesheet" href="https://fonts.googleapis.com/css2?family=Cinzel:wght@400;700&family=Marcellus&display=swap">
<style>
  :root {
    --backdrop: #a9c2dc;
    --paper: #ffffff;
    --paper-tint: #eef4fb;
    --navy: #1f3f73;
    --slate: #5a6a7e;
    --grey: #8a8a8e;
    --sky: #d6e9f6;
    --sky-soft: #e6f1fa;
    --ink: #26344a;
  }
  * { margin: 0; padding: 0; box-sizing: border-box; }
  html, body { width: 1200px; height: 784px; overflow: hidden; }
  body { background: var(--backdrop); position: relative; }

  .letterhead {
    position: absolute; left: 322px; top: 32px;
    width: 556px; height: 720px;
    background: radial-gradient(ellipse at 60% 45%, var(--paper) 40%, var(--paper-tint) 100%);
    box-shadow: 0 6px 18px rgba(30, 60, 100, 0.25);
    overflow: hidden;
  }

  .firm-mark {
    position: absolute; left: 40px; top: 42px;
    display: flex; align-items: center; gap: 10px;
  }
  .firm-mark__square { width: 26px; height: 26px; background: var(--navy); flex: none; }
  .firm-mark__name {
    font-family: "Cinzel", serif; font-weight: 700;
    font-size: 20px; line-height: 1; color: var(--navy); letter-spacing: 0.5px;
    white-space: nowrap;
  }
  .firm-tagline {
    position: absolute; left: 76px; top: 74px;
    font-family: "Marcellus", serif; font-size: 7.5px;
    letter-spacing: 1.6px; color: var(--slate); text-transform: uppercase;
    white-space: nowrap;
  }

  .contact-tiles { position: absolute; right: 0; top: 60px; width: 140px; height: 140px; }

  .contact-block {
    position: absolute; right: 30px; top: 44px;
    font-family: "Marcellus", serif; font-style: normal;
    font-size: 8px; color: var(--ink); line-height: 13px;
    white-space: nowrap;
  }
  .contact-block__firm {
    font-family: "Cinzel", serif; font-weight: 700;
    font-size: 9.5px; color: var(--navy); margin-bottom: 3px;
  }
  .contact-block__line { display: flex; align-items: center; gap: 5px; text-transform: uppercase; letter-spacing: 0.3px; }
  .contact-block__line--indent { padding-left: 13px; }
  .contact-block__icon { width: 8px; height: 8px; flex: none; }

  .corner-swoosh { position: absolute; left: 0; bottom: 0; width: 556px; height: 420px; }

  .footer-band { position: absolute; left: 0; bottom: 0; width: 100%; height: 9px; display: flex; }
  .footer-band__main { flex: 1; background: var(--navy); }
  .footer-band__gap { width: 4px; background: var(--paper); }
  .footer-band__accent { width: 110px; background: var(--grey); }
</style>
</head>
<body>
  <main class="letterhead">
    <svg class="corner-swoosh" viewBox="0 0 556 420" aria-hidden="true">
      <path d="M0 40 C 60 220, 300 330, 556 400 L556 420 L0 420 Z" fill="#e9f2fb"/>
      <path d="M30 0 C 40 170, 200 260, 420 300" fill="none" stroke="var(--sky)" stroke-width="10"/>
      <path d="M10 30 C 50 210, 260 310, 556 380" fill="none" stroke="var(--sky-soft)" stroke-width="14"/>
    </svg>

    <div class="firm-mark">
      <span class="firm-mark__square"></span>
      <span class="firm-mark__name">Tallow &amp; Mersey</span>
    </div>
    <div class="firm-tagline">Attorneys at Law / Founded in 1990</div>

    <svg class="contact-tiles" viewBox="0 0 140 140" aria-hidden="true">
      <rect x="40" y="20" width="70" height="55" fill="var(--sky-soft)"/>
      <rect x="80" y="60" width="60" height="60" fill="var(--sky)" opacity="0.7"/>
      <rect x="30" y="85" width="55" height="45" fill="var(--sky-soft)"/>
    </svg>

    <address class="contact-block">
      <div class="contact-block__firm">Tallow &amp; Mersey, LLP</div>
      <div class="contact-block__line">
        <svg class="contact-block__icon" viewBox="0 0 10 10"><circle cx="5" cy="5" r="5" fill="var(--navy)"/><circle cx="5" cy="4" r="1.8" fill="#fff"/></svg>
        7183 Corvid Lane, Suite 640
      </div>
      <div class="contact-block__line contact-block__line--indent">Brenford, OK 75591</div>
      <div class="contact-block__line">
        <svg class="contact-block__icon" viewBox="0 0 10 10"><circle cx="5" cy="5" r="5" fill="var(--navy)"/><rect x="3.5" y="2.5" width="3" height="5" rx="0.8" fill="#fff"/></svg>
        Tel: (555) 408-1936
      </div>
      <div class="contact-block__line">
        <svg class="contact-block__icon" viewBox="0 0 10 10"><circle cx="5" cy="5" r="5" fill="var(--navy)"/><rect x="2.5" y="3.5" width="5" height="3.5" fill="#fff"/></svg>
        Fax: (555) 408-2275
      </div>
      <div class="contact-block__line">
        <svg class="contact-block__icon" viewBox="0 0 10 10"><circle cx="5" cy="5" r="5" fill="var(--navy)"/><circle cx="5" cy="5" r="2.6" fill="none" stroke="#fff" stroke-width="0.9"/></svg>
        www.tallowandmersey.example
      </div>
    </address>

    <div class="footer-band">
      <span class="footer-band__main"></span>
      <span class="footer-band__gap"></span>
      <span class="footer-band__accent"></span>
    </div>
  </main>
</body>
</html>
```